Willow Bend Senior Care

Just had our logo redesigned and want to get all supporting collateral, business cards, postcards, brochure, etc to go together, but the business cards are the current priority.
We are an agency who provides care for seniors to help them with activities of daily living and companionship in their own home. I have attached our color guidelines and our logo, as well as a copy of our current card for your reference. Our clients are seniors 65+ We would like to see something somewhat conservative but creative (we are getting rid of the desert background), double sided full color (back should have our mission statement and services as it does in the current one) Thanks a million for looking! I am looking forward to seeing what you come up with!
Target Market(s)
65+ baby boomers and 80+ Seniors
Industry/Entity Type
Conservative

```html
<!DOCTYPE html>
<html lang="en">
<head>
<meta charset="utf-8">
<title>Willow Bend Senior Care – Business Cards</title>
<link rel="stylesheet" href="https://fonts.googleapis.com/css2?family=Montserrat:wght@400;500;700&family=Oswald:wght@500&display=swap">
<style>
  :root {
    --bg: #e6e7e9;
    --card: #ffffff;
    --navy: #1d4b86;
    --green: #6db33f;
    --ink: #3b4452;
    --muted: #6b7480;
    --rule: #9fb6cf;
  }
  * { box-sizing: border-box; margin: 0; padding: 0; }
  html, body { width: 1200px; height: 988px; overflow: hidden; }
  body {
    background: var(--bg);
    font-family: "Montserrat", Arial, sans-serif;
    color: var(--ink);
    position: relative;
  }
  .card {
    position: absolute;
    left: 220px;
    width: 760px;
    height: 434px;
    background: var(--card);
    box-shadow: 0 6px 18px rgba(0,0,0,0.12);
  }
  .card--back { top: 44px; }
  .card--front { top: 510px; }

  .brand {
    display: flex;
    align-items: center;
    gap: 14px;
  }
  .brand__name {
    font-weight: 700;
    color: var(--navy);
    letter-spacing: -0.5px;
    white-space: nowrap;
  }
  .brand__dot {
    border-radius: 50%;
    background: var(--green);
    flex: none;
  }

  /* Back */
  .card--back .brand {
    position: absolute;
    left: 0; right: 0; top: 92px;
    justify-content: center;
  }
  .card--back .brand__name { font-size: 40px; }
  .card--back .brand__dot { width: 34px; height: 34px; }

  .mission {
    position: absolute;
    left: 110px; right: 110px; top: 170px;
    text-align: center;
    font-size: 14px;
    line-height: 1.6;
    color: var(--ink);
    font-style: normal;
  }
  .mission-rule {
    position: absolute;
    left: 300px; right: 300px; top: 252px;
    height: 1px;
    background: var(--rule);
  }
  .services {
    position: absolute;
    left: 150px; right: 150px; top: 276px;
    list-style: none;
    display: grid;
    grid-template-columns: 1fr 1fr;
    column-gap: 40px;
    row-gap: 12px;
    font-size: 13px;
    color: var(--ink);
  }
  .service {
    display: flex;
    align-items: center;
    gap: 10px;
  }
  .service::before {
    content: "";
    width: 8px; height: 8px;
    border-radius: 50%;
    background: var(--green);
    flex: none;
  }

  /* Front */
  .card--front .brand {
    position: absolute;
    left: 46px; top: 58px;
  }
  .card--front .brand__name { font-size: 34px; }
  .card--front .brand__dot { width: 28px; height: 28px; }

  .header-rule {
    position: absolute;
    left: 46px; right: 40px; top: 122px;
    height: 1px;
    background: var(--rule);
  }

  .person {
    position: absolute;
    left: 46px; top: 168px;
  }
  .person__name {
    font-family: "Oswald", "Arial Narrow", sans-serif;
    font-weight: 500;
    font-size: 25px;
    color: var(--navy);
    letter-spacing: 0.5px;
    text-transform: uppercase;
  }
  .person__role {
    font-size: 11px;
    letter-spacing: 1.5px;
    text-transform: uppercase;
    color: var(--muted);
    margin-top: 2px;
  }

  .contact-list {
    position: absolute;
    list-style: none;
  }
  .contact-list--left { left: 46px; top: 246px; width: 320px; }
  .contact-list--right { left: 420px; top: 150px; width: 300px; }
  .contact {
    display: flex;
    align-items: center;
    gap: 12px;
    height: 44px;
    border-bottom: 1px solid var(--rule);
    font-size: 13px;
    color: var(--ink);
  }
  .contact + .contact { margin-top: 4px; }
  .contact__icon {
    width: 26px; height: 26px;
    background: var(--navy);
    border-radius: 4px;
    flex: none;
    display: flex;
    align-items: center;
    justify-content: center;
  }
  .contact__icon svg { width: 16px; height: 16px; }
</style>
</head>
<body>

  <section class="card card--back" aria-label="Business card back">
    <div class="brand">
      <span class="brand__name">Willow Bend Senior Care</span>
      <span class="brand__dot"></span>
    </div>
    <p class="mission">Our mission is to help seniors live safely, comfortably and with dignity in their own homes, through caring support and warm companionship.</p>
    <div class="mission-rule"></div>
    <ul class="services">
      <li class="service">Companionship &amp; Conversation</li>
      <li class="service">Bathing &amp; Personal Care</li>
      <li class="service">Meal Planning &amp; Preparation</li>
      <li class="service">Light Housekeeping</li>
      <li class="service">Medication Reminders</li>
      <li class="service">Errands &amp; Transportation</li>
    </ul>
  </section>

  <section class="card card--front" aria-label="Business card front">
    <div class="brand">
      <span class="brand__name">Willow Bend Senior Care</span>
      <span class="brand__dot"></span>
    </div>
    <div class="header-rule"></div>

    <div class="person">
      <p class="person__name">Daniel Harper</p>
      <p class="person__role">Care Director</p>
    </div>

    <ul class="contact-list contact-list--left">
      <li class="contact">
        <span class="contact__icon">
          <svg viewBox="0 0 16 16" fill="#fff"><path d="M4 1.5l2.3 2.6-1.2 1.8c.8 1.8 2.2 3.2 4 4l1.8-1.2 2.6 2.3-1.3 2.4C7 13.2 2.8 9 1.6 2.8z"/></svg>
        </span>
        012 555 0148
      </li>
      <li class="contact">
        <span class="contact__icon">
          <svg viewBox="0 0 16 16" fill="none" stroke="#fff" stroke-width="1.5"><rect x="4.5" y="1.5" width="7" height="13" rx="1.2"/><line x1="7" y1="12" x2="9" y2="12"/></svg>
        </span>
        012 555 0172
      </li>
      <li class="contact">
        <span class="contact__icon">
          <svg viewBox="0 0 16 16" fill="#fff"><path d="M8 1a5 5 0 0 0-5 5c0 3.6 5 9 5 9s5-5.4 5-9a5 5 0 0 0-5-5zm0 7a2 2 0 1 1 0-4 2 2 0 0 1 0 4z"/></svg>
        </span>
        21 Meadow Lane, Suite 4, Riverton
      </li>
    </ul>

    <ul class="contact-list contact-list--right">
      <li class="contact">
        <span class="contact__icon">
          <svg viewBox="0 0 16 16" fill="none" stroke="#fff" stroke-width="1.4"><rect x="1.5" y="3.5" width="13" height="9" rx="1"/><path d="M1.8 4l6.2 5 6.2-5"/></svg>
        </span>
        hello@willowbendcare.com
      </li>
      <li class="contact">
        <span class="contact__icon">
          <svg viewBox="0 0 16 16" fill="none" stroke="#fff" stroke-width="1.3"><circle cx="8" cy="8" r="6.3"/><ellipse cx="8" cy="8" rx="2.8" ry="6.3"/><line x1="1.7" y1="8" x2="14.3" y2="8"/></svg>
        </span>
        www.willowbendcare.com
      </li>
    </ul>
  </section>

</body>
</html>
```